Landing Page for z7 airport parking

The site will be called Q9 parking

We basically need a lead collector for airport parking. It should be a one page site with a form on it .

Info

Compare Cheap Airport Parking

Compare prices of car parking at all UK airports with our unbiased search engine and save money by booking in advance.

What we offer?

We are the cheapest that’s guaranteed! Q9 Parking compares cheap airport parking from almost all the car parks servicing UK airports plus…

Free comparison engine to find the best deal for you.
All types of car parking including Valet, Long Stay, Short Stay and Hotels with parking.
We guarantee you won’t find cheaper for the same product or service.
Your car parking space or hotel room is guaranteed.
Quick check out with prepaid vouchers.
Savings on published prices with easy and secure booking process.
What type of car parking?

There are four types of parking product we provide, On-Airport, Off-Airport, Valet Meet & Greet and Hotel parking.

On-Airport Parking

This is our most popular option. On-airport parking is the most convenient self park option. Its usually within a few minutes transfer time from the airport terminal and allows you to keep your car keys while abroad.

Off-Airport Parking

Similar to On-Airport parking but further away from the airport terminal making it less expensive. Also, the car park will keep your car keys so that they can block park your car in a secure compound. Transfer time to the airport is usually 10-15 minutes.

Meet & Greet Parking

This is the premium car parking service. You just drive up to the airport terminal to be met and greeted by a Valet Chauffeur who will park your car for you usually in one of the Off-Airport car parks. This is the most stress and hassle free option and great if you have lots of luggage or cumbersome items such as skis, snowboards, buggies etc.

Airport Hotel with Parking

If you’re worried about getting to the airport on time or have an early/late flight then booking into an airport hotel with parking the night before or after your flight is a very relaxing option. Especially if you have a long drive ahead of you, knowing that you can rest in a comfortable hotel before or after your flight is a most appealing option to some travellers. See it as an enjoyable extension to your holiday or business trip.

Target Market(s)

People travelling from a uk airport and will need parking

Industry/Entity Type

Airport

Font styles to use
Sans Serif

Requirements
Must have
• The form should ask.
• Flying From:
• Parking from:
• Returning to collect car
• Full Name:
• Address:
• Dob:
• Phone:
• And Search Button
Nice to have
• One Page Lading Page only No other pages everything should be on one page. Parallax is fine.

```html
<!DOCTYPE html>
<html lang="en">
<head>
<meta charset="utf-8">
<title>Q9 Parking — Compare Cheap Airport Parking</title>
<link href="https://fonts.googleapis.com/css2?family=Lato:wght@400;700&display=swap" rel="stylesheet">
<style>
  :root {
    --yellow: #f6c21a;
    --yellow-deep: #efb90f;
    --ink: #2b2b2b;
    --dark: #333333;
    --grey-text: #555555;
    --light-bg: #f7f7f5;
    --white: #ffffff;
    --field-border: #e2e2e2;
    --muted: #bdbdbd;
  }
  * { box-sizing: border-box; margin: 0; padding: 0; }
  html, body { width: 1200px; height: 2228px; overflow: hidden; }
  body { position: relative; font-family: 'Lato', sans-serif; color: var(--ink); background: var(--white); }

  .site-header { position: absolute; left: 0; top: 0; width: 1200px; height: 100px; background: var(--white); }
  .brand { position: absolute; left: 172px; top: 28px; display: flex; align-items: center; gap: 12px; }
  .brand-name { font-size: 34px; font-weight: 700; color: var(--yellow); letter-spacing: 0.5px; }
  .brand-mark { width: 18px; height: 18px; background: var(--ink); }
  .follow { position: absolute; right: 172px; top: 18px; display: flex; align-items: center; gap: 5px; font-size: 11px; font-weight: 700; color: var(--ink); }
  .follow span { margin-right: 4px; }
  .social-square { width: 20px; height: 20px; background: var(--muted); border-radius: 2px; }
  .search { position: absolute; left: 548px; top: 50px; width: 219px; height: 30px; border: 1px solid var(--field-border); display: flex; align-items: center; padding: 0 12px; font-size: 12px; color: #c8c8c8; justify-content: space-between; }
  .btn { display: flex; align-items: center; justify-content: center; font-weight: 700; text-transform: uppercase; color: var(--white); border-radius: 3px; }
  .btn-contact { position: absolute; left: 772px; top: 50px; width: 127px; height: 30px; background: var(--yellow); font-size: 12px; }
  .btn-book { position: absolute; left: 902px; top: 50px; width: 126px; height: 30px; background: #3c3c3c; font-size: 12px; }

  .hero { position: absolute; left: 0; top: 100px; width: 1200px; height: 428px; }
  .hero-photo { position: absolute; inset: 0; background: radial-gradient(ellipse at 50% 55%, #d8c51a 0%, #9d8d10 45%, #4a430a 100%); }
  .main-nav { position: absolute; left: 172px; top: 0; width: 856px; height: 45px; display: flex; }
  .main-nav a { width: 171px; display: flex; align-items: center; justify-content: center; color: var(--white); text-decoration: none; font-size: 12px; font-weight: 700; text-transform: uppercase; }
  .main-nav a.active { background: rgba(40,40,40,0.85); }
  .hero-title { position: absolute; left: 320px; top: 142px; width: 560px; text-align: center; color: var(--white); font-size: 27px; line-height: 32px; font-weight: 400; text-transform: uppercase; }
  .scroll-cue { position: absolute; left: 50%; transform: translateX(-50%); }

  .welcome { position: absolute; left: 0; top: 528px; width: 1200px; height: 308px; background: var(--light-bg); text-align: center; }
  .section-title { font-size: 29px; font-weight: 400; text-transform: uppercase; }
  .section-title em { font-style: normal; color: var(--yellow); }
  .welcome .section-title { position: absolute; left: 0; width: 1200px; top: 56px; color: var(--ink); }
  .welcome-copy { position: absolute; left: 208px; width: 784px; top: 102px; font-size: 13.5px; line-height: 24px; color: var(--grey-text); }

  .compare { position: absolute; left: 0; top: 836px; width: 1200px; height: 426px; }
  .compare-photo { position: absolute; inset: 0; background: linear-gradient(90deg, #1a1a1a 0%, #3a3a3a 30%, #454545 50%, #3a3a3a 70%, #2a1618 100%); }
  .compare .section-title { position: absolute; left: 0; width: 1200px; top: 64px; text-align: center; color: var(--yellow); }
  .compare-list { position: absolute; left: 0; width: 1200px; top: 108px; list-style: none; text-align: center; color: var(--white); font-size: 14.5px; line-height: 24px; }
  .btn-compare { position: absolute; left: 495px; top: 286px; width: 210px; height: 36px; background: var(--yellow); font-size: 12px; border-radius: 0; }

  .offer { position: absolute; left: 0; top: 1262px; width: 1200px; height: 426px; background: var(--white); text-align: center; }
  .offer .section-title { position: absolute; left: 0; width: 1200px; top: 44px; color: var(--ink); }
  .offer-intro { position: absolute; left: 0; width: 1200px; top: 86px; font-size: 12px; color: var(--grey-text); }
  .offer-grid { position: absolute; left: 191px; top: 126px; width: 818px; height: 244px; display: flex; gap: 2px; }
  .offer-card { position: relative; flex: 1; overflow: hidden; }
  .offer-photo { position: absolute; inset: 0; }
  .photo-on { background: linear-gradient(160deg, #6e7378, #3c3f42); }
  .photo-off { background: linear-gradient(180deg, #4a5358, #2c3236); }
  .photo-greet { background: linear-gradient(160deg, #a7a7a7, #5a5a5a); }
  .photo-hotel { background: linear-gradient(160deg, #777, #3a3a3a); }
  .offer-name { position: absolute; left: 0; width: 100%; bottom: 28px; color: var(--white); font-size: 22px; line-height: 26px; font-weight: 400; }
  .offer-card.featured .offer-name { top: 28px; bottom: auto; }
  .offer-detail { position: absolute; left: 0; bottom: 0; width: 100%; height: 130px; background: rgba(246,194,26,0.92); padding: 16px 22px 0; color: var(--white); font-size: 11.5px; line-height: 19px; font-weight: 700; }
  .btn-learn { width: 110px; height: 30px; margin: 12px auto 0; background: #333; font-size: 12px; text-transform: none; border-radius: 0; }

  .reservation { position: absolute; left: 0; top: 1688px; width: 1200px; height: 453px; }
  .reservation-photo { position: absolute; inset: 0; background: radial-gradient(ellipse at 60% 75%, #e4b212 0%, var(--yellow) 55%, var(--yellow-deep) 100%); }
  .reservation .section-title { position: absolute; left: 0; width: 1200px; top: 62px; text-align: center; color: var(--ink); }
  .reservation-intro { position: absolute; left: 0; width: 1200px; top: 106px; text-align: center; font-size: 12px; color: var(--grey-text); }
  .reservation-form { position: absolute; left: 193px; top: 149px; width: 815px; display: grid; grid-template-columns: repeat(3, 264px); column-gap: 11px; row-gap: 12px; }
  .reservation-form label { display: flex; align-items: center; height: 32px; background: var(--white); border: 1px solid var(--field-border); padding: 0 14px; font-size: 9px; color: #9a9a9a; text-transform: uppercase; }
  .btn-reserve { position: absolute; left: 484px; top: 307px; width: 232px; height: 46px; background: #2e2e2e; font-size: 12px; border-radius: 3px; box-shadow: 0 3px 4px rgba(0,0,0,0.25); }

  .site-footer { position: absolute; left: 0; top: 2141px; width: 1200px; height: 87px; background: var(--white); }
  .copyright { position: absolute; left: 172px; top: 38px; font-size: 12px; color: var(--grey-text); }
  .footer-social { position: absolute; right: 172px; top: 34px; display: flex; gap: 7px; }
  .footer-social .social-square { width: 21px; height: 21px; background: #c9c9c9; }
</style>
</head>
<body>

<header class="site-header">
  <div class="brand"><span class="brand-name">Q9 Parking</span><span class="brand-mark"></span></div>
  <div class="follow"><span>Follow Us:</span><i class="social-square"></i><i class="social-square"></i><i class="social-square"></i><i class="social-square"></i></div>
  <div class="search">Search
    <svg width="13" height="13" viewBox="0 0 13 13"><circle cx="5.5" cy="5.5" r="4" fill="none" stroke="#f6c21a" stroke-width="1.6"/><line x1="8.5" y1="8.5" x2="12" y2="12" stroke="#f6c21a" stroke-width="1.8"/></svg>
  </div>
  <a class="btn btn-contact">Contact Us</a>
  <a class="btn btn-book">Book Now!</a>
</header>

<section class="hero">
  <div class="hero-photo" role="img" aria-label="Underground airport car park lit in yellow with parked cars"></div>
  <nav class="main-nav">
    <a class="active">Home</a><a>About Us</a><a>Compare</a><a>What We Offer?</a><a>Reservation Form</a>
  </nav>
  <h1 class="hero-title">We are the cheapest that’s guaranteed! Q9 Parking compares cheap airport parking from almost all the car parks servicing UK airports …</h1>
  <svg class="scroll-cue" style="top:356px" width="26" height="34" viewBox="0 0 26 34" fill="#fff"><circle cx="13" cy="3" r="1.6"/><circle cx="13" cy="9" r="1.6"/><circle cx="13" cy="15" r="1.6"/><circle cx="3" cy="18" r="1.6"/><circle cx="23" cy="18" r="1.6"/><circle cx="7" cy="23" r="1.6"/><circle cx="19" cy="23" r="1.6"/><circle cx="13" cy="22" r="1.6"/><circle cx="10" cy="28" r="1.6"/><circle cx="16" cy="28" r="1.6"/><circle cx="13" cy="32" r="1.6"/></svg>
</section>

<section class="welcome">
  <h2 class="section-title">Welcome <em>to Q9 Parking</em></h2>
  <div class="welcome-copy">
    <p>Lorem ipsum dolor sit amet, consectetuer adipiscing elit, sed diam nonummy nibh euismod tincidunt ut laoreet dolore magna aliquam erat volutpat. Ut wisi enim ad minim veniam, quis nostrud exerci tation ullamcorper suscipit lobortis nisl ut aliquip ex ea commodo consequat.</p>
    <p>Duis autem vel eum iriure dolor in hendrerit in vulputate velit esse molestie consequat, vel illum dolore eu feugiat nulla facilisis at vero eros et accumsan et iusto odio dignissim qui blandit praesent luptatum zzril delenit augue duis dolore te feugait nulla facilisi.</p>
  </div>
  <svg class="scroll-cue" style="top:250px" width="26" height="34" viewBox="0 0 26 34" fill="#f6c21a"><circle cx="13" cy="3" r="1.6"/><circle cx="13" cy="9" r="1.6"/><circle cx="13" cy="15" r="1.6"/><circle cx="3" cy="18" r="1.6"/><circle cx="23" cy="18" r="1.6"/><circle cx="7" cy="23" r="1.6"/><circle cx="19" cy="23" r="1.6"/><circle cx="13" cy="22" r="1.6"/><circle cx="10" cy="28" r="1.6"/><circle cx="16" cy="28" r="1.6"/><circle cx="13" cy="32" r="1.6"/></svg>
</section>

<section class="compare">
  <div class="compare-photo" role="img" aria-label="Dark tarmac with airport parking lettering between parked cars"></div>
  <h2 class="section-title">Compare</h2>
  <ul class="compare-list">
    <li>Free comparison engine to find the best deal for you.</li>
    <li>All types of car parking including Valet, Long Stay, Short Stay and Hotels with parking.</li>
    <li>We guarantee you won’t find cheaper for the same product or service.</li>
    <li>Your car parking space or hotel room is guaranteed.</li>
    <li>Quick check out with prepaid vouchers.</li>
    <li>Savings on published prices with easy and secure booking process.</li>
  </ul>
  <a class="btn btn-compare">Compare Prices</a>
  <svg class="scroll-cue" style="top:358px" width="26" height="34" viewBox="0 0 26 34" fill="#fff"><circle cx="13" cy="3" r="1.6"/><circle cx="13" cy="9" r="1.6"/><circle cx="13" cy="15" r="1.6"/><circle cx="3" cy="18" r="1.6"/><circle cx="23" cy="18" r="1.6"/><circle cx="7" cy="23" r="1.6"/><circle cx="19" cy="23" r="1.6"/><circle cx="13" cy="22" r="1.6"/><circle cx="10" cy="28" r="1.6"/><circle cx="16" cy="28" r="1.6"/><circle cx="13" cy="32" r="1.6"/></svg>
</section>

<section class="offer">
  <h2 class="section-title">What We Offer?</h2>
  <p class="offer-intro">There are four types of parking product we provide, On-Airport, Off-Airport, Valet Meet &amp; Greet and Hotel parking.</p>
  <div class="offer-grid">
    <article class="offer-card">
      <div class="offer-photo photo-on" role="img" aria-label="Aerial view of an open-air airport car park"></div>
      <h3 class="offer-name">On-Airport<br>Parking</h3>
    </article>
    <article class="offer-card featured">
      <div class="offer-photo photo-off" role="img" aria-label="Covered multi-storey car park"></div>
      <h3 class="offer-name">Off-Airport<br>Parking</h3>
      <div class="offer-detail">Similar to On-Airport parking but further away from the airport terminal making it less expensive.
        <a class="btn btn-learn">Learn More</a>
      </div>
    </article>
    <article class="offer-card">
      <div class="offer-photo photo-greet" role="img" aria-label="Hand holding out car keys"></div>
      <h3 class="offer-name">Meet &amp; Greet<br>Parking</h3>
    </article>
    <article class="offer-card">
      <div class="offer-photo photo-hotel" role="img" aria-label="Marked parking bays on dark tarmac"></div>
      <h3 class="offer-name">Airport Hotel<br>with Parking</h3>
    </article>
  </div>
</section>

<section class="reservation">
  <div class="reservation-photo" role="img" aria-label="Faint aeroplane taking off over a yellow sky"></div>
  <h2 class="section-title">Reservation Form</h2>
  <p class="reservation-intro">All types of car parking including Valet, Long Stay, Short Stay and Hotels with parking</p>
  <form class="reservation-form">
    <label>Flying From:</label>
    <label>Parking From:</label>
    <label>Returning to collect car</label>
    <label>Full Name:</label>
    <label>Address:</label>
    <label>DOB:</label>
    <label>Phone:</label>
    <label>E-mail:</label>
    <label>Date:</label>
  </form>
  <a class="btn btn-reserve">Make a Reservation</a>
</section>

<footer class="site-footer">
  <p class="copyright">© 2014. Q9 Parking. All Rights Reserved.</p>
  <div class="footer-social"><i class="social-square"></i><i class="social-square"></i><i class="social-square"></i><i class="social-square"></i></div>
</footer>

</body>
</html>
```